Wedding Photography business card

I need a business card made for a wedding photography business. Formal, unique, i like dark colors maybe black, white, gray, deep blue, silver. Sharp.

This is an idea i have i don't know if it would work.
Think Palm Beach, florida

work in mirror mode in your design program, Just an idea

Front side:
feminine, classy maybe white from wedding dress,
script, elegant,

back side:
masculine, black from tux, symbolizing strength, power,
serif

RV Photography
(555) 214-3097
www.ruthvlenses.example

Target Market(s)

upscale Weddings, targeting bride and groom

Industry/Entity Type

Wedding

Font styles to use
Serif
Script

Colors

Designer to choose colors to be used in the design.

Requirements
Must have
• both sides match somehow

```html
<!DOCTYPE html>
<html lang="en">
<head>
<meta charset="utf-8">
<title>RV Photography — Business Card</title>
<link rel="stylesheet" href="https://fonts.googleapis.com/css2?family=Cormorant+Garamond:wght@500&family=Josefin+Sans:wght@300&display=swap">
<style>
  :root {
    --backdrop: #e9e6df;
    --paper: #f1eee6;
    --paper-edge: #d9d4c8;
    --ink: #2b2a26;
    --tux: #262621;
    --tux-pattern: #3a382f;
    --silk: #f4f2ec;
  }
  * { box-sizing: border-box; margin: 0; padding: 0; }
  html, body {
    width: 1200px;
    height: 750px;
    overflow: hidden;
    background: var(--backdrop);
  }
  .sheet {
    width: 1200px;
    height: 750px;
    display: flex;
    align-items: center;
    justify-content: center;
    gap: 60px;
  }
  .card {
    width: 525px;
    height: 300px;
    position: relative;
    overflow: hidden;
    box-shadow: 0 10px 26px rgba(40, 36, 28, 0.18);
  }

  /* Front: bride side */
  .card--front {
    background: var(--paper);
    border: 1px solid var(--paper-edge);
  }
  .card--front .lace-texture {
    position: absolute;
    inset: 0;
    background: linear-gradient(135deg, #f3f0e9 0%, #ece8de 100%);
  }
  .front-content {
    position: relative;
    height: 100%;
    display: flex;
    flex-direction: column;
    align-items: center;
    justify-content: center;
    color: var(--ink);
    text-align: center;
  }
  .wordmark {
    font-family: "Cormorant Garamond", serif;
    font-weight: 500;
    font-size: 34px;
    letter-spacing: 0.04em;
    margin-bottom: 30px;
  }
  .person-name {
    font-family: "Cormorant Garamond", serif;
    font-weight: 500;
    font-variant: small-caps;
    font-size: 22px;
    letter-spacing: 0.08em;
    margin-bottom: 8px;
  }
  .contact-line {
    font-family: "Josefin Sans", sans-serif;
    font-weight: 300;
    font-size: 15px;
    letter-spacing: 0.06em;
    line-height: 1.6;
  }

  /* Back: groom side */
  .card--back { background: var(--tux); }
  .tux-pattern {
    position: absolute;
    left: 0;
    width: 100%;
    background: var(--tux-pattern);
  }
  .tux-pattern--top { top: 0; height: 115px; }
  .tux-pattern--bottom { bottom: 0; height: 55px; }
  .back-band {
    position: absolute;
    left: 0;
    right: 0;
    top: 115px;
    bottom: 55px;
    display: flex;
    align-items: center;
    justify-content: flex-end;
    padding-right: 42px;
  }
  .back-band .wordmark {
    color: var(--silk);
    font-size: 32px;
    margin: 0;
  }
</style>
</head>
<body>
  <main class="sheet">
    <section class="card card--front" aria-label="Card front">
      <div class="lace-texture" role="img" aria-label="Faint white interlocking lace pattern across the card"></div>
      <div class="front-content">
        <p class="wordmark">RV Photography</p>
        <p class="person-name">Ruth Vance</p>
        <p class="contact-line">(555) 214-3097</p>
        <p class="contact-line">www.ruthvlenses.example</p>
      </div>
    </section>

    <section class="card card--back" aria-label="Card back">
      <div class="tux-pattern tux-pattern--top" role="img" aria-label="Interlocking circle pattern in muted bronze on black"></div>
      <div class="back-band">
        <p class="wordmark">RV Photography</p>
      </div>
      <div class="tux-pattern tux-pattern--bottom" role="img" aria-label="Interlocking circle pattern in muted bronze on black"></div>
    </section>
  </main>
</body>
</html>
```